Personal Business Card Design Project

I am looking for a business card to be able to hand to both Chinese and Australian businessman.
I am a self employed consultant and just need my name, phone number and email address on the card. No Business Name and No Website.
I want it to look like an exclusive prestigious card.
I would like the background to be be a glossy red and the writing to be gold. (This applies to both sides of the card).
It must have English on one side and Chinese (Mandarin) on the reverse.
Details you will require
Name : Wade Emmerson
Phone : + 61 493 207 158
Email : wadeyemmerson@brightpost.example
Thank you everybody for your designs.
Industry/Entity Type
Business

```html
<!DOCTYPE html>
<html lang="en">
<head>
<meta charset="utf-8">
<title>Wade Emmerson – Consultant</title>
<link rel="stylesheet" href="https://fonts.googleapis.com/css2?family=Jost:wght@200;300&display=swap">
<style>
  :root {
    --card-red: #c4001a;
    --gold: #e6bd45;
    --gold-contact: #e9b838;
  }
  html, body {
    margin: 0;
    padding: 0;
    width: 1200px;
    height: 734px;
    overflow: hidden;
    background: var(--card-red);
  }
  .business-card {
    display: block;
    width: 1200px;
    height: 734px;
    background: var(--card-red);
  }
  .card-text {
    font-family: "Jost", "Century Gothic", sans-serif;
  }
  .name-line,
  .title-line {
    fill: var(--gold);
    font-weight: 200;
    letter-spacing: 1px;
  }
  .contact-line {
    fill: var(--gold-contact);
    font-weight: 200;
    letter-spacing: 0.3px;
  }
</style>
</head>
<body>
<svg class="business-card" viewBox="0 0 1200 734" xmlns="http://www.w3.org/2000/svg" role="img" aria-label="Business card for Wade Emmerson, Consultant">
  <rect width="1200" height="734" fill="var(--card-red)"/>

  <g class="card-text identity-block">
    <text class="name-line" x="305" y="218" font-size="84">Wade Emmerson</text>
    <text class="title-line" x="360" y="378" font-size="84">Consultant</text>
  </g>

  <g class="card-text contact-block">
    <text class="contact-line phone" x="200" y="662" font-size="46">Phone: + 61 493 207 158</text>
    <text class="contact-line email" x="200" y="716" font-size="46">E-mail:&#160;&#160;wadeyemmerson@brightpost.example</text>
  </g>
</svg>
</body>
</html>
```